ASL Learning Website Application Pages Redesign

Introduction:
We need a redesign of the internal pages of our website, SignTrellis.com. The current website design has been in place for many years and is not mobile friendly. We want an updated design that makes the site look cleaner, more professional, and mobile accessible. We are looking for a design that eliminates the clutter on each page, and makes the site simple and easy to use. We will be interested in your design if it is unique and creative. Don't be afraid to completely change the look of the site.

We need the designs sliced up into clean HTML files that are responsive and work well on both mobile and desktop computers. We will implement the PHP needed to make the pages functional.

About Us:
SignTrellis is a subscription-based website for American Sign Language (ASL) video lessons. The content is for anyone who wishes to learn ASL, regardless of age. It has been designed to instruct Deaf students, parents of Deaf children, and the community-at-large. All lessons are taught by Deaf experts of ASL.

Overview:
The website before log-in does not need any changes. There are five key pages within the internal website (after log-in) that need to be redesigned; they are listed below. Note that some pages (Dictionary and Activity) have multiple sub-pages, so there are about 6-8 pages in total to design, depending on how you decide to approach this (more info in the pages’ respective instruction documents).

The new page designs should retain their existing features, and as stated before, should be mobile friendly. However, you may combine, collapse, or completely change the look of these features. Each page to redesign has a separate instruction document attachment, and screenshots of the current version of the page. Our logo has also been attached. If you want to see the website pages for yourself, you can also go to our website (SignTrellis.com) and use a free trial to get access to the internal site.

As for design preferences, we want our site to be modern-looking and mature. We’re looking for an inviting, educational style that can attract both high school students and adults. We’re happy with the current font and color scheme, but we’re always open to ideas!

Additional Notes:
- Every page has the same header and footer. You could keep these the same, or change them, based on your discretion.
- Currently, every page also has a breadcrumb. The breadcrumb is unnecessary and you may remove it. However, the “add/remove from favorites” button on the right of the breadcrumb is necessary to keep somewhere on the page.

Pages:
Here’s a list of the five key pages we need redesigned:
- Dashboard
- Dictionary
- Lesson
- Activity
- All Lessons

Each page has its own instruction document. These are attached separately.

Just purchased a $150 for Top designers. I need to give them time to submit their designs . Can I have 7 more days?

Target Market(s)

Deaf students, parents of Deaf children, and the community-at-large interested in learning ASL

Coding

Coded - Design and coding required

Number of Pages Required

5+ page

Font styles to use
Sans Serif

Requirements
Must have
• Responsive design - the full application experience should be available on mobile devices.
Follow the directions on the design brief.
Nice to have
• Be creative! Please play around with, or even completely change, the look of the site.

```html
<!DOCTYPE html>
<html lang="en">
<head>
<meta charset="utf-8">
<title>SignTrellis – Lesson Pages</title>
<link href="https://fonts.googleapis.com/css2?family=Lato:wght@300;400;700;900&display=swap" rel="stylesheet">
<style>
:root{
  --green:#62a72f;
  --orange:#ee8000;
  --orange-soft:#f6a94f;
  --cream:#f8f1e2;
  --ink:#2c2c2c;
  --muted:#777;
  --stage:#777777;
  --white:#fff;
  --rule:#d9d9d9;
}
*{margin:0;padding:0;box-sizing:border-box}
html,body{width:1200px;height:1016px;overflow:hidden;background:var(--stage);font-family:"Lato",sans-serif;color:var(--ink)}
.page{position:absolute;top:27px;width:560px;background:var(--white);overflow:hidden}
.page--colour{left:28px;height:960px}
.page--chances{left:613px;height:833px}
.abs{position:absolute}

/* header */
.site-header{position:absolute;left:0;top:0;width:560px;height:52px;background:var(--green)}
.brand{position:absolute;left:0;top:0;width:211px;height:52px;background:var(--cream);display:flex;align-items:center;justify-content:center;gap:5px}
.brand__mark{width:9px;height:9px;background:var(--green)}
.brand__name{font-size:22px;font-weight:700;color:var(--green);letter-spacing:-.3px}
.brand::after{content:"";position:absolute;right:-6px;top:20px;border-left:6px solid var(--cream);border-top:6px solid transparent;border-bottom:6px solid transparent}
.site-header__title{position:absolute;left:247px;top:8px;font-size:9px;font-weight:900;color:var(--white);letter-spacing:-.2px}
.login__field{position:absolute;top:27px;width:90px;height:15px;background:var(--white);border:1px solid #e2e2e2;font-size:5px;color:#aaa;padding:4px 5px}
.login__submit{position:absolute;left:437px;top:27px;width:36px;height:15px;border-radius:8px;background:var(--orange);color:var(--white);font-size:6.5px;font-weight:900;display:flex;align-items:center;justify-content:center}
.login__forgot{position:absolute;left:479px;top:28px;font-size:5.5px;line-height:7.5px;color:var(--white)}
.nav{position:absolute;left:0;top:52px;width:560px;height:21px;background:var(--orange);display:flex;align-items:center;padding-left:73px;gap:12.5px}
.nav a{font-size:7.4px;font-weight:700;color:var(--white);text-decoration:none;white-space:nowrap}
.caret{display:inline-block;margin-left:2px;border-top:3px solid var(--white);border-left:2.5px solid transparent;border-right:2.5px solid transparent;vertical-align:1px}

/* lesson heading */
.lesson-title{position:absolute;top:96px;font-size:16.5px;font-weight:700;color:var(--ink);letter-spacing:-.2px}
.level{position:absolute;top:95px;height:21px;border-radius:11px;background:var(--green);color:var(--white);font-size:8px;font-weight:700;display:flex;align-items:center;justify-content:center}
.resource{position:absolute;top:127px;width:162px;height:29px;border:1px solid var(--orange);color:var(--orange);font-size:8px;display:flex;align-items:center;justify-content:center}
.hint{position:absolute;top:180px;font-size:6.2px;color:var(--ink)}

/* vocabulary */
.vocab{position:absolute;left:47px;top:197px;width:257px;display:grid;grid-template-columns:repeat(3,79px);column-gap:9.5px;row-gap:8px}
.vocab span{height:24px;border:1px solid var(--green);border-radius:12px;color:var(--green);font-size:6.8px;font-weight:700;display:flex;align-items:center;justify-content:center}
.video{position:absolute;left:319px;top:192px;width:195px;height:192px;background:linear-gradient(135deg,#6b4a32 0%,#a8714a 45%,#d8b08a 70%,#8a5a3a 100%)}
.video__play{position:absolute;left:88px;top:87px;width:19px;height:19px;border-radius:50%;background:rgba(255,255,255,.9)}
.video__play::after{content:"";position:absolute;left:7px;top:5px;border-left:7px solid #555;border-top:4.5px solid transparent;border-bottom:4.5px solid transparent}

/* activities */
.section-title{position:absolute;left:0;width:560px;text-align:center;font-size:16.5px;font-weight:700}
.card{position:absolute;width:109px;height:105px;border-radius:5px;background:var(--orange);color:var(--white);text-align:center;padding-top:11px}
.card__num{font-size:30px;font-weight:900;line-height:30px;color:var(--orange-soft)}
.card__name{height:41px;margin-top:4px;font-size:8px;line-height:15px;font-weight:400;padding:0 2px}
.card__meta{font-size:8px;line-height:12px}
.card__start{position:absolute;left:0;right:0;bottom:12px;font-size:6.8px;font-weight:900}
.card--tracked .card__name{height:auto;line-height:13px}
.card--tracked .card__start{bottom:14px}

/* footer */
.footer{position:absolute;left:0;width:560px;height:210px;border-top:2px solid var(--green)}
.footer__brand{position:absolute;left:51px;top:22px;display:flex;align-items:center;gap:4px}
.footer__brand .brand__name{font-size:19px}
.footer__about{position:absolute;left:51px;top:62px;width:130px;font-size:5.4px;line-height:11.6px;color:var(--muted)}
.footer__divider{position:absolute;top:16px;width:1px;height:96px;background:var(--rule)}
.footer__heading{position:absolute;top:15px;font-size:9.5px;font-weight:700}
.footer__list{position:absolute;top:32px;list-style:none;font-size:5.4px;line-height:11.6px;color:var(--muted)}
.contact{position:absolute;left:380px;top:32px;font-size:5.4px;color:var(--muted);list-style:none}
.contact li{display:flex;align-items:center;gap:5px;height:17.5px}
.contact svg{width:6px;height:6px;fill:var(--green)}
.footer__rule{position:absolute;left:51px;top:168px;width:457px;height:1px;background:var(--rule)}
.footer__legal{position:absolute;left:51px;top:180px;font-size:5.4px;line-height:11.6px;color:var(--muted)}
.social{position:absolute;left:409px;top:178px;display:flex;gap:5.5px}
.social span{width:15px;height:15px;border:1px solid #bbb;border-radius:50%;position:relative}
.social span::after{content:"";position:absolute;left:5px;top:5px;width:3px;height:3px;border-radius:50%;background:var(--green)}
.footer__code{position:absolute;left:532px;top:188px;font-size:5.4px;color:var(--ink)}
</style>
</head>
<body>

<!-- Lesson: Colour -->
<section class="page page--colour">
  <header class="site-header">
    <div class="brand"><span class="brand__mark"></span><span class="brand__name">SignTrellis</span></div>
    <div class="site-header__title">HOW TO LEARN ASL THROUGH VIDEO LESSONS ONLINE</div>
    <div class="login__field" style="left:248px">User Name or E-mail</div>
    <div class="login__field" style="left:343px">Password</div>
    <div class="login__submit">SIGN IN</div>
    <div class="login__forgot">Forgot<br>Password</div>
  </header>
  <nav class="nav">
    <a>Home</a><a>Gift Certificates</a><a>For Educators<span class="caret"></span></a><a>Contact Us<span class="caret"></span></a><a>How It Works</a><a>Buy Now</a><a>TRY IT FREE</a><a>Our APP</a>
  </nav>

  <h1 class="lesson-title" style="left:45px">LESSON : COLOUR</h1>
  <div class="level" style="left:196px;width:65px">BEGINNER</div>
  <a class="resource" style="left:46px">View Optional Expressive Skills Exercises</a>
  <a class="resource" style="left:214px">View Warm-up Exercises</a>

  <p class="hint" style="left:46px">Click On each word below before Starting Activites</p>
  <div class="vocab">
    <span>COLOR</span><span>LIGHT (COLOR)</span><span>RED</span>
    <span>GREEN</span><span>PINK</span><span>TAN</span>
    <span>GREY</span><span>DARK (COLOR)</span><span>DARK RED</span>
    <span>LIGHT GREEN</span><span>BRIGHT PINK</span><span>BROWN</span>
    <span>ORANGE</span><span>WHITE</span><span>SILVER</span>
    <span>PURPLE</span><span>GOLD</span><span>BLACK</span>
    <span>BLUE</span><span>YELLOW</span>
  </div>
  <div class="video" role="img" aria-label="Lesson video still: students studying together in a library"><span class="video__play"></span></div>

  <h2 class="section-title" style="top:453px">ACTIVITIES</h2>
  <div class="card card--tracked" style="left:52px;top:488px"><div class="card__num">1</div><div class="card__name">MATCH THE VOCABULARY</div><div class="card__meta">Last Attempted</div><div class="card__meta">05/25/2021 &nbsp;&nbsp; Score:100%</div><div class="card__start">START ACTIVITY</div></div>
  <div class="card" style="left:168px;top:488px"><div class="card__num">2</div><div class="card__name">CHOOSE THE CORRECT<br>SENTENCE</div><div class="card__start">START ACTIVITY</div></div>
  <div class="card" style="left:283px;top:488px"><div class="card__num">3</div><div class="card__name">MATCH THE<br>VOCABULARY</div><div class="card__start">START ACTIVITY</div></div>
  <div class="card" style="left:399px;top:488px"><div class="card__num">4</div><div class="card__name">DAILOGUE<br>ILLUSTRATION</div><div class="card__start">START ACTIVITY</div></div>
  <div class="card" style="left:52px;top:600px"><div class="card__num">5</div><div class="card__name">GRAMMAR<br>INSTRUCTION</div><div class="card__start">START ACTIVITY</div></div>
  <div class="card" style="left:168px;top:600px"><div class="card__num">6</div><div class="card__name">CHOOSE THE<br>CORRECT HANDSHAPE</div><div class="card__start">START ACTIVITY</div></div>
  <div class="card" style="left:283px;top:600px"><div class="card__num">7</div><div class="card__name">ENGLISH TO ASL<br>PRACTICE</div><div class="card__start">START ACTIVITY</div></div>
  <div class="card" style="left:399px;top:600px"><div class="card__num">8</div><div class="card__name">CHOOSE THE CORRECT<br>LOCATION</div><div class="card__start">START ACTIVITY</div></div>

  <footer class="footer" style="top:749px">
    <div class="footer__brand"><span class="brand__mark"></span><span class="brand__name">SignTrellis</span></div>
    <p class="footer__about">SignTrellis is a subscription based website for American Sign Language (ASL) video lessons. The content is for anyone who wishes to learn ASL, regardless of age. It has been designed to instruct Deaf students, parents of Deaf children, and the community-at-large. You may cancel your subscription at any time. All lessons are taught by Deaf experts of ASL.</p>
    <span class="footer__divider" style="left:189px"></span>
    <span class="footer__divider" style="left:367px"></span>
    <h3 class="footer__heading" style="left:207px">Quick Links</h3>
    <ul class="footer__list" style="left:207px"><li>Home</li><li>Try it Free</li><li>Contact Us</li></ul>
    <ul class="footer__list" style="left:286px"><li>Group Rate Form</li><li>Teacher's Guide</li><li>Gift Certificates</li><li>FAQs</li><li>Privacy Policy</li></ul>
    <h3 class="footer__heading" style="left:380px">Contact Us</h3>
    <ul class="contact">
      <li><svg viewBox="0 0 10 10"><path d="M5 0a3.5 3.5 0 0 0-3.5 3.5C1.5 6 5 10 5 10s3.5-4 3.5-6.5A3.5 3.5 0 0 0 5 0zm0 5a1.5 1.5 0 1 1 0-3 1.5 1.5 0 0 1 0 3z"/></svg>PO Box 5820, Maple Ridge, MI 48099</li>
      <li><svg viewBox="0 0 10 10"><path d="M2 0l2 2.5-1 1.5c.7 1.3 1.7 2.3 3 3l1.5-1L10 8 8.5 10C4 9.5.5 6 0 1.5z"/></svg>(555) 014-2273</li>
      <li><svg viewBox="0 0 10 10"><path d="M0 2h10v6H0zM0 2l5 3.5L10 2" stroke="#fff" stroke-width=".8"/></svg>hello@signtrellis.com</li>
    </ul>
    <span class="footer__rule"></span>
    <p class="footer__legal">Copyrights © 2021, SignTrellis. All rights reserved. Terms &amp; Conditions<br>Z: 0.43 sec</p>
    <div class="social"><span></span><span></span><span></span><span></span><span></span></div>
    <span class="footer__code">C 43</span>
  </footer>
</section>

<!-- Lesson: Taking Chances -->
<section class="page page--chances">
  <header class="site-header">
    <div class="brand"><span class="brand__mark"></span><span class="brand__name">SignTrellis</span></div>
    <div class="site-header__title">HOW TO LEARN ASL THROUGH VIDEO LESSONS ONLINE</div>
    <div class="login__field" style="left:248px">User Name or E-mail</div>
    <div class="login__field" style="left:343px">Password</div>
    <div class="login__submit">SIGN IN</div>
    <div class="login__forgot">Forgot<br>Password</div>
  </header>
  <nav class="nav">
    <a>Home</a><a>Gift Certificates</a><a>For Educators<span class="caret"></span></a><a>Contact Us<span class="caret"></span></a><a>How It Works</a><a>Buy Now</a><a>TRY IT FREE</a><a>Our APP</a>
  </nav>

  <h1 class="lesson-title" style="left:31px">LESSON : TAKING CHANCES</h1>
  <div class="level" style="left:249px;width:66px">5TH LEVEL</div>
  <a class="resource" style="left:32px;width:161px">View Teacher's Lesson Plan</a>
  <a class="resource" style="left:200px;width:161px">View Curriculum Standards</a>
  <a class="resource" style="left:367px;width:161px">View Optional Expressive Skills Exercises</a>

  <p class="hint" style="left:47px">Click On each word below before Starting Activites</p>
  <div class="vocab">
    <span>LOREM IPSUM</span><span>LOREM IPSUM</span><span>LOREM IPSUM</span>
    <span>LOREM IPSUM</span><span>LOREM IPSUM</span><span>LOREM IPSUM</span>
    <span>LOREM IPSUM</span><span>LOREM IPSUM</span><span>LOREM IPSUM</span>
    <span>LOREM IPSUM</span><span>LOREM IPSUM</span><span>LOREM IPSUM</span>
    <span>LOREM IPSUM</span><span>LOREM IPSUM</span><span>LOREM IPSUM</span>
    <span>LOREM IPSUM</span><span>LOREM IPSUM</span><span>LOREM IPSUM</span>
  </div>
  <div class="video" role="img" aria-label="Lesson video still: students studying together in a library"><span class="video__play"></span></div>

  <h2 class="section-title" style="top:434px">ACTIVITIES</h2>
  <div class="card card--tracked" style="left:111px;top:469px"><div class="card__num">1</div><div class="card__name">MATCH THE VOCABULARY</div><div class="card__meta">Last Attempted</div><div class="card__meta">05/25/2021 &nbsp;&nbsp; Score:100%</div><div class="card__start">START ACTIVITY</div></div>
  <div class="card" style="left:226px;top:469px"><div class="card__num">2</div><div class="card__name">CHOOSE THE CORRECT<br>SENTENCE</div><div class="card__start">START ACTIVITY</div></div>
  <div class="card" style="left:342px;top:469px"><div class="card__num">3</div><div class="card__name">MATCH THE<br>VOCABULARY</div><div class="card__start">START ACTIVITY</div></div>

  <footer class="footer" style="top:623px">
    <div class="footer__brand"><span class="brand__mark"></span><span class="brand__name">SignTrellis</span></div>
    <p class="footer__about">SignTrellis is a subscription based website for American Sign Language (ASL) video lessons. The content is for anyone who wishes to learn ASL, regardless of age. It has been designed to instruct Deaf students, parents of Deaf children, and the community-at-large. You may cancel your subscription at any time. All lessons are taught by Deaf experts of ASL.</p>
    <span class="footer__divider" style="left:189px"></span>
    <span class="footer__divider" style="left:367px"></span>
    <h3 class="footer__heading" style="left:208px">Quick Links</h3>
    <ul class="footer__list" style="left:208px"><li>Home</li><li>Try it Free</li><li>Contact Us</li></ul>
    <ul class="footer__list" style="left:286px"><li>Group Rate Form</li><li>Teacher's Guide</li><li>Gift Certificates</li><li>FAQs</li><li>Privacy Policy</li></ul>
    <h3 class="footer__heading" style="left:380px">Contact Us</h3>
    <ul class="contact">
      <li><svg viewBox="0 0 10 10"><path d="M5 0a3.5 3.5 0 0 0-3.5 3.5C1.5 6 5 10 5 10s3.5-4 3.5-6.5A3.5 3.5 0 0 0 5 0zm0 5a1.5 1.5 0 1 1 0-3 1.5 1.5 0 0 1 0 3z"/></svg>PO Box 5820, Maple Ridge, MI 48099</li>
      <li><svg viewBox="0 0 10 10"><path d="M2 0l2 2.5-1 1.5c.7 1.3 1.7 2.3 3 3l1.5-1L10 8 8.5 10C4 9.5.5 6 0 1.5z"/></svg>(555) 014-2273</li>
      <li><svg viewBox="0 0 10 10"><path d="M0 2h10v6H0zM0 2l5 3.5L10 2" stroke="#fff" stroke-width=".8"/></svg>hello@signtrellis.com</li>
    </ul>
    <span class="footer__rule" style="top:169px"></span>
    <p class="footer__legal" style="top:181px">Copyrights © 2021, SignTrellis. All rights reserved. Terms &amp; Conditions<br>Z: 0.43 sec</p>
    <div class="social" style="top:179px"><span></span><span></span><span></span><span></span><span></span></div>
    <span class="footer__code" style="top:189px">C 43</span>
  </footer>
</section>

</body>
</html>
```